WEBSITE DESIGN, VELTRA paint and panel

We are in need of a website for Veltra Paint & Panel based in Brisbane, Australia. We are a boutique Automotive Paint & Panel Company that provides services to all makes and models of vehicles. We have attached a logo that is still in draft stage but gives you an idea of the colour scheme and fonts and overall impact we are looking for. We are after a white background so this is clean and crisp whilst being sleek, modern and professional. The website must represent our slogan of Flawless shade on the Finest frame. The website must therefore be visually effective as our product is to get colour and placement on vehicle body's correct so the website must have this impact on our clients. We are after a widescreen webpage that is simple and logical to navigate. The final design should give clients the confidence that we can deliver on our promise.
Updates

Target Market(s)

Vehicle Owners who have a need for panel repairs and people who want to reinvigorate their car with a new coat of paint.

Industry/Entity Type

Car Repair

Coding

Coded - Design and coding required

Number of Pages Required

5+ page

Font styles to use
Sans Serif

Colors
ffffff
ffc214
000000

Requirements
Must have
• Page 1 - Home Page
• Page 2 - Our Process
• Page 3 - Private Customers
• Page 4 - Fleet & Corporate
• Page 5 - Insurance
• Page 6 - Get a Quote
• Page 7 - Connect (Contacts Page)
• Same font and colour scheme as the logo.
Should not have
• A typical mechanical/paint and panel layout which looks like a template website.

```html
<!DOCTYPE html>
<html lang="en">
<head>
<meta charset="utf-8">
<title>Veltra Paint &amp; Panel</title>
<link href="https://fonts.googleapis.com/css2?family=Raleway:wght@400;500;600;700;800&family=Open+Sans:wght@400;600&display=swap" rel="stylesheet">
<style>
:root{
  --blue:#3354bd;
  --blue-deep:#2a469f;
  --ink:#222;
  --dark:#2b2b2b;
  --darker:#1e1e1e;
  --grey:#777;
  --light:#f4f4f4;
  --white:#fff;
  --yellow:#ffc214;
}
*{box-sizing:border-box;margin:0;padding:0}
html,body{width:709px;height:1200px;overflow:hidden;background:var(--white)}
body{font-family:"Open Sans",Arial,sans-serif;color:var(--ink);position:relative}
h1,h2,h3,h4,.logo,.nav a{font-family:"Raleway",Arial,sans-serif}

.topbar{height:18px;background:var(--darker);color:#ccc;font-size:6.5px;display:flex;align-items:center;justify-content:space-between;padding:0 70px}
.topbar .contact span{margin-right:16px;display:inline-flex;align-items:center;gap:3px}
.topbar .account span{margin-left:12px}
.dot{width:6px;height:6px;border-radius:50%;background:var(--blue);display:inline-block}

.nav{height:54px;background:var(--white);display:flex;align-items:stretch;justify-content:center;padding:0 50px;border-bottom:1px solid #eee}
.nav ul{list-style:none;display:flex;align-items:stretch}
.nav a{display:flex;align-items:center;padding:0 13px;font-size:7px;font-weight:600;color:#333;text-decoration:none;height:100%}
.nav a.active{background:var(--dark);color:var(--white)}
.logo{display:flex;flex-direction:column;align-items:center;justify-content:center;padding:0 24px}
.logo .mark{display:flex;align-items:center;gap:5px;font-size:20px;font-weight:800;letter-spacing:3px;color:var(--ink)}
.logo .mark i{width:10px;height:10px;background:var(--blue);display:block}
.logo small{font-size:5.5px;letter-spacing:2px;color:var(--grey);text-transform:uppercase;margin-top:1px}

.hero{position:relative;height:286px;background:linear-gradient(100deg,#d9dde3 0%,#8e959f 30%,#3b3f47 60%,#1c1f25 100%);overflow:hidden;border-bottom:3px solid var(--blue)}
.hero .scene{position:absolute;inset:0}
.hero .scene-gun{position:absolute;right:0;top:0;width:320px;height:100%;background:radial-gradient(circle at 60% 45%,#f0e7e0 0%,#9aa5c4 25%,rgba(50,70,140,.35) 55%,transparent 75%)}
.hero h1{position:absolute;left:24px;top:52px;font-size:19px;font-weight:500;color:var(--blue);letter-spacing:.2px}

.divider{position:relative;height:30px}
.divider .diamond{position:absolute;left:50%;top:-9px;width:18px;height:18px;background:var(--blue);transform:translateX(-50%) rotate(45deg)}
.divider svg{position:absolute;left:50%;top:-4px;transform:translateX(-50%)}

.welcome{text-align:center;padding:8px 70px 0;height:157px}
.welcome h2{font-size:17px;font-weight:600;color:var(--ink)}
.welcome h2 em{font-style:normal;color:var(--blue)}
.welcome p{font-size:6.5px;color:var(--grey);line-height:1.6;margin:10px auto 0;max-width:570px}
.btn{display:inline-block;background:var(--blue);color:var(--white);font-size:6.5px;padding:5px 14px;margin-top:14px;font-family:"Raleway",Arial,sans-serif}

.services{display:flex;height:275px}
.services .panel{width:354px;background:var(--blue);padding:20px 22px 0 60px;color:var(--white)}
.services h2{font-size:17px;font-weight:500;text-align:right;padding-right:12px;margin-bottom:12px}
.services h2 b{font-weight:600;color:var(--yellow)}
.service{display:flex;align-items:flex-start;gap:10px;margin-bottom:18px}
.service .text{flex:1;text-align:right}
.service h3{font-size:7.5px;font-weight:700;margin-bottom:3px}
.service p{font-size:5.8px;line-height:1.55;color:#dfe5f7}
.service .icon{width:24px;height:24px;border:1.5px solid var(--white);border-radius:50%;flex-shrink:0;display:flex;align-items:center;justify-content:center}
.services .photo{flex:1;background:linear-gradient(135deg,#dfe3ea 0%,#8d98ad 40%,#3d4f85 75%,#c9ccd2 100%)}

.testimonial{display:flex;height:138px}
.testimonial .photo{width:270px;background:linear-gradient(135deg,#f2d36b 0%,#6a86c9 45%,#2e3f7a 100%)}
.testimonial .quote{flex:1;background:var(--blue-deep);color:var(--white);padding:24px 30px 0 22px;display:flex;gap:14px}
.testimonial .qmark{font-family:"Raleway",Arial,sans-serif;font-size:40px;line-height:.8;font-weight:800}
.testimonial p{font-size:6.5px;line-height:1.65;color:#e3e8f8}
.testimonial .author{display:flex;align-items:center;gap:8px;justify-content:center;margin-top:14px;font-size:8px;font-family:"Raleway",Arial,sans-serif}
.testimonial .author i{width:24px;height:1px;background:var(--white);display:block}

.footer{height:197px;background:var(--dark);color:#bbb;display:flex;padding:28px 24px 0;gap:40px}
.footer .col{flex:1}
.footer h4{font-size:11px;font-weight:500;color:var(--white);margin-bottom:10px}
.footer p{font-size:6px;line-height:1.65}
.footer .label{color:var(--white);font-size:6.5px;margin-top:6px}
.social{display:flex;gap:5px;margin-top:12px}
.social span{width:13px;height:13px;background:var(--blue)}
.subscribe{display:flex;margin-top:12px}
.subscribe span{flex:1;height:14px;background:var(--white);font-size:5.5px;color:#999;padding:4px 5px}
.subscribe b{background:var(--blue);color:var(--white);font-size:5.5px;font-weight:600;padding:4px 8px}

.bottom{height:35px;background:var(--darker);color:#999;font-size:6px;display:flex;align-items:center;justify-content:space-between;padding:0 24px}
</style>
</head>
<body>

<header>
  <div class="topbar">
    <div class="contact"><span><i class="dot"></i>Call us: +0700 555 218</span><span><i class="dot"></i>Mail us at: info@veltrapaint.example</span></div>
    <div class="account"><span>Login</span><span>Register</span></div>
  </div>
  <nav class="nav">
    <ul>
      <li><a class="active">Home</a></li>
      <li><a>Our Process</a></li>
      <li><a>Private Customers</a></li>
    </ul>
    <div class="logo"><div class="mark"><i></i>VELTRA</div><small>paint and panel</small></div>
    <ul>
      <li><a>Fleet &amp; Corporate Services</a></li>
      <li><a>Get a Quote</a></li>
      <li><a>Connect</a></li>
    </ul>
  </nav>
</header>

<section class="hero">
  <div class="scene" role="img" aria-label="Car body outline with a spray gun applying blue paint">
    <div class="scene-gun"></div>
  </div>
  <h1>Flawless Shade On The Finest Frame</h1>
</section>

<div class="divider">
  <div class="diamond"></div>
  <svg width="10" height="6" viewBox="0 0 10 6"><path d="M1 1l4 4 4-4" fill="none" stroke="#fff" stroke-width="1.5"/></svg>
</div>

<section class="welcome">
  <h2>Welcome To <em>Veltra Paint &amp; Panel</em></h2>
  <p>We restore and refinish vehicles of every make and model with factory-matched colour, careful panel alignment and a finish that lasts. Our Brisbane workshop blends skilled hands with modern spray booths, computer colour matching and premium coatings, so every repair looks as though it never happened. From minor scratches to full resprays, we treat each car as if it were our own and return it on time, clean and ready for the road.</p>
  <span class="btn">Read more</span>
</section>

<section class="services">
  <div class="panel">
    <h2>Our <b>Service</b></h2>
    <div class="service">
      <div class="text"><h3>Best in speed</h3><p>Most repairs are assessed, quoted and booked in within a day, with clear updates at every stage until your car is ready.</p></div>
      <div class="icon"><svg width="12" height="12" viewBox="0 0 12 12"><circle cx="6" cy="6" r="4.5" fill="none" stroke="#fff"/><path d="M6 3v3l2 1.5" fill="none" stroke="#fff"/></svg></div>
    </div>
    <div class="service">
      <div class="text"><h3>Best in services</h3><p>Friendly staff guide you through insurance, fleet and private work, keeping paperwork simple and communication honest.</p></div>
      <div class="icon"><svg width="12" height="12" viewBox="0 0 12 12"><path d="M2 6.5l2.5 2.5L10 3" fill="none" stroke="#fff" stroke-width="1.3"/></svg></div>
    </div>
    <div class="service">
      <div class="text"><h3>Best Automotive Paint</h3><p>Computer colour matching and premium coatings give a deep, even gloss that blends perfectly with every surrounding panel.</p></div>
      <div class="icon"><svg width="12" height="12" viewBox="0 0 12 12"><path d="M2 8l1.5-3h5L10 8v2H2z M4 10v1 M8 10v1" fill="none" stroke="#fff"/></svg></div>
    </div>
  </div>
  <div class="photo" role="img" aria-label="Two mechanics in blue overalls beside an open car bonnet"></div>
</section>

<section class="testimonial">
  <div class="photo" role="img" aria-label="Two smiling workshop technicians"></div>
  <div class="quote">
    <div class="qmark">&ldquo;</div>
    <div>
      <p>The team brought my ten-year-old sedan back to showroom condition. The colour match is perfect, the panels line up beautifully and the car was ready a day early. I would not take it anywhere else.</p>
      <div class="author"><i></i>Dorian Kell</div>
    </div>
  </div>
</section>

<footer>
  <div class="footer">
    <div class="col">
      <h4>About Our Company</h4>
      <p>A boutique Brisbane paint and panel workshop caring for all makes and models with precise colour and careful craftsmanship.</p>
      <div class="social"><span></span><span></span><span></span></div>
    </div>
    <div class="col">
      <h4>Contact Us</h4>
      <div class="label">Phone us</div>
      <p>+61 7 3000 4821 / 3000 4822</p>
      <div class="label">Address</div>
      <p>12 Fairlane Street, Brisbane QLD 4000</p>
    </div>
    <div class="col">
      <h4>News Letter</h4>
      <p>Join our list for seasonal offers, care tips and workshop news.</p>
      <div class="subscribe"><span>Email</span><b>SUBSCRIBE</b></div>
    </div>
  </div>
  <div class="bottom"><span>copyright@2016VELTRA</span><span>TOP</span></div>
</footer>

</body>
</html>
```